Plumvale CEO needs a Crowdsourced Graphic for a Wirelark Article

I need a simple graphic / banner for a blog post that's going to be posted on Wirelark (www.wirelark.com) - the biggest tech blog in the world.

The article will be written by Tobin Marsh (Plumvale's CEO) and the title will be "Asia's Secret Crowdsourcing Boom". The article is about the tens of thousands of people using crowdsourcing websites (like Plumvale.com, Qorvel.com and Vantrio.com) in China, India, the Philippines, Australia and other countries in the Asia Pacific region.

We'd really like to get this ASAP - so early submissions encouraged. We will try and get the winning designer linked to from the article.

Thanks to everyone that submitted!  Some great designs and hard to choose! :)

Target Market(s)

Tech saavy readers, English speakers

Industry/Entity Type

Tech

Requirements
Must have
• The graphic SHOULD:
1) Have the text "Asia's secret crowdsourcing boom" with some nice design and fonts (consider grey subtle pattern background and white drop shadow on fonts) - see attached examples
2) Have an Asian theme
3) Have the dimensions 640px wide by 240px wide
Nice to have
• The graphic COULD:
1) Have references to some or all of the countries mentioned above or use Asian characters as part of the background / motif (maybe the word "crowd" or "crowd sourcing" in different languages). In Chinese, the word for crowdsourcing is "witkey" (and there are corresponding Chinese characters: ??)
2) Emphasize the word "Asia" (using color and larger/different font)
3) Use a chart showing exponential (i.e. fast) growth - like the attached
4) Have a second line of text "5 Things You Didn't Know About Crowdsourcing in Asia"

```html
<!DOCTYPE html>
<html lang="en">
<head>
<meta charset="utf-8">
<title>Asia's Secret Crowdsourcing Boom</title>
<link rel="stylesheet" href="https://fonts.googleapis.com/css2?family=Marcellus+SC&family=Questrial&family=Shojumaru&display=swap">
<style>
  :root {
    --grey-dark: #7d7d7d;
    --grey-light: #b4b4b4;
    --red-deep: #6e0000;
    --red-dark: #9c0000;
    --red-mid: #c20a0a;
    --red-bright: #e01a12;
    --red-hot: #f03a1c;
    --accent-red: #d01010;
    --badge-orange: #ff8a3a;
    --badge-red: #e8200c;
    --ink: #1a1a1a;
    --paper: #ffffff;
  }
  * { margin: 0; padding: 0; box-sizing: border-box; }
  html, body { width: 1200px; height: 450px; overflow: hidden; background: var(--paper); }
  .banner { position: relative; width: 1200px; height: 450px; overflow: hidden; background: var(--paper); }
  .hero-backdrop { position: absolute; left: 0; top: 0; width: 1200px; height: 345px; display: block; }
  .hero-title {
    position: absolute; left: 40px; top: 48px; width: 900px;
    font-family: "Marcellus SC", serif; font-size: 82px; line-height: 88px;
    text-transform: uppercase; font-weight: 400;
    color: var(--paper); text-align: center; letter-spacing: 3px;
    text-shadow: 0 0 6px rgba(255,255,255,0.9), 0 0 14px rgba(255,255,255,0.55), 2px 3px 4px rgba(0,0,0,0.35);
  }
  .divider { position: absolute; left: 0; top: 343px; width: 1200px; height: 5px; background: var(--accent-red); }
  .subtitle {
    position: absolute; left: 9px; top: 358px;
    font-family: "Questrial", sans-serif; font-size: 42px; line-height: 42px;
    color: var(--ink); letter-spacing: 3px; white-space: nowrap;
  }
  .subtitle .highlight { color: var(--accent-red); }
  .asia-word {
    position: absolute; left: 652px; top: 364px;
    font-family: "Shojumaru", cursive; font-size: 84px; line-height: 84px;
    color: var(--accent-red); letter-spacing: 10px;
  }
  .accent-disc {
    position: absolute; left: 919px; top: 160px; width: 215px; height: 215px; border-radius: 50%;
    background: radial-gradient(circle at 50% 30%, var(--badge-orange) 0%, var(--badge-red) 75%);
  }
</style>
</head>
<body>
<main class="banner">
  <svg class="hero-backdrop" viewBox="0 0 1200 345" preserveAspectRatio="none" aria-hidden="true">
    <defs>
      <linearGradient id="grey-field" x1="0" y1="0" x2="1" y2="1">
        <stop offset="0" stop-color="var(--grey-dark)"/>
        <stop offset="1" stop-color="var(--grey-light)"/>
      </linearGradient>
    </defs>
    <rect width="1200" height="345" fill="url(#grey-field)"/>
    <path d="M860 0 C800 110 680 250 540 345 L1200 345 L1200 0 Z" fill="var(--red-mid)"/>
    <path d="M930 0 C850 130 740 260 620 345 L1200 345 L1200 0 Z" fill="var(--red-deep)"/>
    <path d="M1200 20 C1060 110 880 250 700 345 L1200 345 Z" fill="var(--red-dark)"/>
    <path d="M1200 90 C1080 160 920 270 790 345 L1200 345 Z" fill="var(--red-mid)"/>
    <path d="M1200 150 C1090 210 960 290 880 345 L1200 345 Z" fill="var(--red-bright)"/>
    <path d="M1200 220 C1120 260 1030 310 980 345 L1200 345 Z" fill="var(--red-hot)"/>
  </svg>

  <h1 class="hero-title">Asia's Secret<br>Crowdsourcing<br>Boom</h1>

  <div class="divider"></div>

  <p class="subtitle">5 THINGS YOU DIDN'T KNOW<br>ABOUT <span class="highlight">CROWDSOURCING</span> IN</p>
  <span class="asia-word">ASIA</span>

  <div class="accent-disc" aria-hidden="true"></div>
</main>
</body>
</html>
```